Single Page Digital Brochure

We are a Sydney based finance company. We lend money to developers. Please see attached example of what we are looking to have produced. We just need a design which can be posted on LINKEDIN

Target Market(s)

Property Developers who are borrowing money

Industry/Entity Type

Finance

Requirements
Must have
• Australian relevant imagery.

TEXT TO INCLUDE:

New Offering from Harlow Ridge Capital
Nice to have
• Design and colour scheme based around our logo (attached)

Please include the same text as the attachment

Please make the design based loosely on the attachment. But do not copy the attachement
Should not have
• Remove Text: 'Settle in under four days'

```html
<!DOCTYPE html>
<html lang="en">
<head>
<meta charset="utf-8">
<title>New Offering from Harlow Ridge Capital</title>
<link href="https://fonts.googleapis.com/css2?family=Montserrat:wght@800&family=Source+Sans+3:wght@300;400;600&display=swap" rel="stylesheet">
<style>
  :root {
    --canvas: #666666;
    --ink: #ffffff;
    --sky: #111821;
    --dusk: #2b3644;
    --city-glow: #6b5a3c;
    --water: #24384a;
    --footer: #000000;
    --brand-green: #2f5e3f;
  }
  * { margin: 0; padding: 0; box-sizing: border-box; }
  html, body {
    width: 1200px; height: 1200px; overflow: hidden;
    background: var(--canvas);
  }
  .brochure {
    position: absolute; left: 120px; top: 335px;
    width: 960px; height: 480px;
    color: var(--ink);
    font-family: "Source Sans 3", sans-serif;
  }
  .hero {
    position: absolute; left: 0; top: 0; width: 960px; height: 389px;
    background:
      linear-gradient(180deg, rgba(12,17,23,0.55) 0%, rgba(12,17,23,0.15) 45%, rgba(12,17,23,0.45) 100%),
      radial-gradient(ellipse 320px 120px at 820px 250px, rgba(140,115,70,0.55), transparent 70%),
      radial-gradient(ellipse 260px 110px at 470px 250px, rgba(90,95,100,0.55), transparent 70%),
      radial-gradient(ellipse 360px 120px at 150px 330px, rgba(60,90,115,0.6), transparent 70%),
      radial-gradient(ellipse 300px 90px at 600px 360px, rgba(45,70,95,0.55), transparent 70%),
      linear-gradient(180deg, var(--sky) 0%, #1c2530 38%, var(--dusk) 62%, var(--water) 100%);
  }
  .headline {
    position: absolute; left: 43px; top: 44px;
    font-family: "Montserrat", sans-serif; font-weight: 800;
    font-size: 49px; line-height: 64px; letter-spacing: -0.5px;
    text-transform: uppercase;
  }
  .deal {
    position: absolute; left: 542px; top: 44px;
    list-style: none;
  }
  .deal-title {
    font-weight: 600; font-size: 27px; line-height: 36px; margin-bottom: 6px;
  }
  .deal-row { font-size: 24px; line-height: 40px; font-weight: 300; white-space: nowrap; }
  .deal-row .label { font-weight: 400; }
  .contact-bar {
    position: absolute; left: 0; top: 389px; width: 960px; height: 91px;
    background: var(--footer);
  }
  .contact {
    position: absolute; left: 43px; top: 14px;
    font-family: "Montserrat", sans-serif; font-size: 23px; line-height: 33px;
  }
  .contact .lead { font-weight: 800; }
  .contact .link { color: var(--brand-green); font-weight: 800; }
  .contact .or { font-family: "Source Sans 3", sans-serif; font-weight: 400; }
  .brand {
    position: absolute; right: 46px; top: 30px;
    display: flex; align-items: center; gap: 10px;
    font-family: "Source Sans 3", sans-serif; font-weight: 600;
    font-size: 20px; color: var(--ink); letter-spacing: 0.5px;
  }
  .brand-dot { width: 16px; height: 16px; border-radius: 50%; background: var(--brand-green); }
</style>
</head>
<body>
  <article class="brochure">
    <div class="hero" role="img" aria-label="Sydney harbour, city skyline and harbour bridge at dusk"></div>

    <h1 class="headline">New<br>Offering<br>From<br>Harlow Ridge<br>Capital</h1>

    <ul class="deal">
      <li class="deal-title">We did. Just last week.</li>
      <li class="deal-row"><span class="label">Loan Amount:</span> $750,000</li>
      <li class="deal-row"><span class="label">Rate:</span> 7.79%</li>
      <li class="deal-row"><span class="label">Term:</span> 12 months</li>
      <li class="deal-row"><span class="label">LVR:</span> 60%</li>
      <li class="deal-row"><span class="label">Repayments:</span> Settled in 4 days</li>
      <li class="deal-row"><span class="label">Security:</span> 2x Sydney Resid Properties</li>
      <li class="deal-row"><span class="label">Purpose:</span> Business Working Capital</li>
    </ul>

    <footer class="contact-bar">
      <p class="contact">
        <span class="lead">Call us today on</span> <span class="link">0298765432</span> <span class="or">or</span><br>
        <span class="link">hello@harlowridgecapital.com.au</span>
      </p>
      <div class="brand"><span class="brand-dot"></span>Harlow Ridge Capital</div>
    </footer>
  </article>
</body>
</html>
```